Harborne Cellarbook: the premier wine registry - (need business cards)

We have a logo designed, and now we need business cards for our 3 founders. Harborne Cellarbook is the premier wine registry for weddings. I am envisioning the wine glass with the heart in it as our signature symbol. (FYI- on the red background file, only use the part that has the red background; the brown colors are not relevant)

```html
<!DOCTYPE html>
<html lang="en">
<head>
<meta charset="utf-8">
<title>Harborne Cellarbook — Business Cards</title>
<link rel="stylesheet" href="https://fonts.googleapis.com/css2?family=Montserrat:wght@400&family=Great+Vibes&family=Cormorant+SC:wght@500&display=swap">
<style>
  :root {
    --backdrop: #ece7e2;
    --wine: #9c2350;
    --wine-deep: #8a1c45;
    --paper: #ffffff;
    --rule: #b66a88;
    --blush: #f3d3dc;
    --ink-light: #fbeff3;
  }
  html, body {
    margin: 0;
    padding: 0;
    width: 1200px;
    height: 906px;
    overflow: hidden;
    background: var(--backdrop);
  }
  .canvas {
    position: relative;
    width: 1200px;
    height: 906px;
  }
  .card {
    position: absolute;
    width: 560px;
    height: 320px;
    background: var(--wine);
    overflow: hidden;
    box-shadow: 0 6px 18px rgba(60, 20, 35, 0.18);
  }
  .card--front { left: 70px; top: 110px; }
  .card--back  { left: 570px; top: 476px; }

  .card__strokes {
    position: absolute;
    inset: 0;
    width: 100%;
    height: 100%;
  }
  .brand {
    position: absolute;
    left: 0;
    right: 0;
    top: 140px;
    display: flex;
    align-items: center;
    justify-content: center;
    gap: 14px;
  }
  .brand__dot {
    width: 14px;
    height: 14px;
    border-radius: 50%;
    background: var(--ink-light);
  }
  .brand__name {
    font-family: "Montserrat", sans-serif;
    font-weight: 400;
    font-size: 27px;
    letter-spacing: 4px;
    color: var(--ink-light);
    text-transform: uppercase;
  }

  .person {
    position: absolute;
    left: 38px;
    top: 62px;
  }
  .person__name {
    font-family: "Great Vibes", cursive;
    font-size: 44px;
    color: var(--blush);
    margin: 0;
    line-height: 1;
  }
  .person__role {
    font-family: "Cormorant SC", serif;
    font-weight: 500;
    font-size: 15px;
    letter-spacing: 1.5px;
    color: var(--ink-light);
    margin: 18px 0 0 14px;
  }
  .contacts {
    position: absolute;
    right: 34px;
    top: 92px;
    margin: 0;
    padding: 0;
    list-style: none;
    text-align: right;
    font-family: "Cormorant SC", serif;
    font-weight: 500;
    font-size: 13.5px;
    letter-spacing: 0.8px;
    line-height: 22px;
    color: var(--ink-light);
  }
</style>
</head>
<body>
<main class="canvas">

  <section class="card card--front" aria-label="Business card front">
    <svg class="card__strokes" viewBox="0 0 560 320" aria-hidden="true">
      <path d="M0 0 H560 V6 C420 28 260 52 0 92 Z" fill="var(--paper)"/>
      <path d="M0 74 C200 48 380 22 560 4 L560 10 C380 30 200 56 0 82 Z" fill="var(--wine)"/>
      <line x1="30" y1="92" x2="530" y2="42" stroke="var(--rule)" stroke-width="1"/>
      <path d="M560 320 H0 V312 C180 300 380 270 560 218 Z" fill="var(--paper)"/>
      <path d="M90 310 C260 294 410 268 560 236 L560 242 C410 276 260 300 90 314 Z" fill="var(--wine)"/>
    </svg>
    <div class="brand">
      <span class="brand__dot" aria-hidden="true"></span>
      <span class="brand__name">Harborne Cellarbook</span>
    </div>
  </section>

  <section class="card card--back" aria-label="Business card back">
    <div class="person">
      <h2 class="person__name">Founder's Name</h2>
      <p class="person__role">Founder</p>
    </div>
    <ul class="contacts">
      <li>Mobile: +123 456 7890</li>
      <li>Landline: +123 456 7890</li>
      <li>Office Address: 123 Street, City, ST 12345</li>
      <li>Email: hello@hcellarbook.com</li>
      <li>Official Website: www.harbornecellarbook.com</li>
      <li>Instagram @harbornecellarbook</li>
    </ul>
  </section>

</main>
</body>
</html>
```